Castaflex Brochure

We need a conference brochure designed with a copy ready for print and also a PDF copy for email usage. We have mocked up something in word with the wording, the specific ads and images are provided in the drop box folder.

https://www.boxlocker.net/sh/qp4ks8e2mn31x07/HtYcLumPQA?n=55120471

Reason: I have extended the deadline and offered more money as we understand the work is required.

```html
<!DOCTYPE html>
<html lang="en">
<head>
<meta charset="utf-8">
<title>Castaflex Conference – Accommodation</title>
<link rel="stylesheet" href="https://fonts.googleapis.com/css2?family=Montserrat:wght@200;300;400;700;800&family=Roboto+Slab:wght@700;800&family=Mulish:wght@400;600&display=swap">
<style>
  :root {
    --backdrop: #fbfbf6;
    --paper: #ffffff;
    --navy: #1d4a6e;
    --ink: #3d3d3d;
    --orange: #f28a1c;
    --blue-text: #2f5f9a;
    --panel: #a9c4e8;
    --panel-ink: #132236;
    --sky: #d6e4f1;
  }
  * { margin: 0; padding: 0; box-sizing: border-box; }
  html, body { width: 1200px; height: 1000px; overflow: hidden; background: var(--backdrop); }
  .canvas { position: relative; width: 1200px; height: 1000px; }
  .page {
    position: absolute; left: 292px; top: 50px; width: 635px; height: 898px;
    background: var(--paper); overflow: hidden;
  }
  .photo { position: absolute; }
  .photo--room {
    left: 0; top: 0; width: 635px; height: 208px;
    background: linear-gradient(100deg, #d9dde0 0%, #f2f2ef 30%, #e8e6e0 55%, #c9b89a 75%, #8fa4c4 88%, #5d6f80 100%);
  }
  .sky-fade {
    position: absolute; left: 0; top: 560px; width: 635px; height: 140px;
    background: linear-gradient(180deg, rgba(214,228,241,0) 0%, var(--sky) 100%);
  }
  .photo--coast {
    left: 0; top: 690px; width: 635px; height: 208px;
    background: linear-gradient(180deg, #dfe8ef 0%, #c9cfcf 18%, #b8b3a6 34%, #5f8fb0 48%, #3c7aa3 65%, #9d9580 80%, #4d7d93 100%);
  }
  .photo--beach {
    left: 285px; top: 420px; width: 350px; height: 118px;
    background: linear-gradient(180deg, #dedcd8 0%, #d8c8ae 35%, #b9a88e 60%, #cdbb9c 75%, #b6c8dd 100%);
  }

  .intro {
    position: absolute; left: 39px; top: 230px; width: 200px;
    font-family: "Mulish", sans-serif; font-size: 11.3px; line-height: 14.2px; color: var(--ink);
  }
  .intro strong { font-weight: 600; color: #111; }

  .headline { position: absolute; right: 39px; top: 252px; text-align: right; }
  .headline__title {
    font-family: "Montserrat", sans-serif; font-weight: 200; font-size: 40px; line-height: 46px;
    color: var(--navy); letter-spacing: 0.5px;
  }
  .headline__venue {
    font-family: "Montserrat", sans-serif; font-weight: 800; font-size: 20px; line-height: 24px;
    color: var(--navy); letter-spacing: 0.3px;
  }
  .headline__price {
    font-family: "Montserrat", sans-serif; font-weight: 800; font-size: 31px; line-height: 34px;
    color: var(--orange);
  }
  .headline__note {
    position: absolute; right: 33px; top: 358px; white-space: nowrap;
    font-family: "Mulish", sans-serif; font-size: 11.5px; color: var(--blue-text);
  }

  .features { position: absolute; left: 37px; top: 406px; width: 210px; }
  .features__title {
    font-family: "Roboto Slab", serif; font-weight: 800; font-size: 18.5px; color: var(--navy);
    margin-bottom: 8px;
  }
  .features__list { list-style: none; padding-left: 17px; }
  .features__list li {
    position: relative;
    font-family: "Roboto Slab", serif; font-weight: 700; font-size: 10.3px; line-height: 12.8px;
    color: var(--navy);
  }
  .features__list li::before {
    content: ""; position: absolute; left: -14px; top: 5px; width: 4px; height: 4px;
    border-radius: 50%; background: var(--navy);
  }

  .booking {
    position: absolute; left: 285px; top: 538px; width: 350px; height: 128px;
    background: var(--panel); padding: 12px 15px;
    font-family: "Mulish", sans-serif; font-weight: 600; font-size: 12.6px; line-height: 15.5px;
    color: var(--panel-ink);
  }
  .booking__link { color: #fff; }
</style>
</head>
<body>
<div class="canvas">
  <div class="page">
    <div class="photo photo--room" role="img" aria-label="Hotel room with two beds, armchair and work desk beside a window"></div>
    <div class="sky-fade"></div>
    <div class="photo photo--coast" role="img" aria-label="Coastal view of a beachside suburb with a rock shelf and blue sea in the foreground"></div>
    <div class="photo photo--beach" role="img" aria-label="Beachfront buildings and hotel along the sand"></div>

    <p class="intro"><strong>Our modern</strong>, contemporary Harbourline Village View exude laid-back, oceanfront ambience. Each room is designed to offer contemporary style and a range of modern comforts including luxurious ensuite bathroom, LCD television and 24 hour in-room dining. Business travellers will enjoy a productive stay with an ergonomic workspace and Wi-Fi internet access at this contemporary Eastern Suburbs hotel.</p>

    <div class="headline">
      <h1 class="headline__title">Accommodation</h1>
      <p class="headline__venue">HARBOURLINE VILLAGE VIEW</p>
      <p class="headline__price">200 AUD</p>
    </div>
    <p class="headline__note">per room per night | upgrades on request</p>

    <section class="features">
      <h2 class="features__title">Room Features</h2>
      <ul class="features__list">
        <li>King bed or two double beds with plush bedding</li>
        <li>Ensuite bathroom with premium amenities and plush bathrobes</li>
        <li>LCD television with Premier Sport channels and movies on demand</li>
        <li>Spacious work desk with ergonomic chair</li>
        <li>Wi-Fi internet access</li>
        <li>Fully stocked minibar</li>
        <li>Radio, clock and alarm</li>
        <li>Hair dryer, iron and ironing board</li>
        <li>In-room temperature control</li>
        <li>Secure in-room safe</li>
        <li>Telephone and voicemail</li>
        <li>Tide and Table 24 hour<br>in-room dining</li>
        <li>Valet laundry and dry cleaning</li>
      </ul>
    </section>

    <div class="booking">
      All accommodation needs to be booked online through the hotel portal.<br>
      Please visit <span class="booking__link">www.castaflexconference.com.au</span><br>
      for the link or contact<br>
      <span class="booking__link">dferrante@castmouldingassoc.com</span><br>
      for assistance.
    </div>
  </div>
</div>
</body>
</html>
```